Fashion Label Startup Business Card Design

Maribel Quint is a startup fashion designer based on the Gold Coast in QLD Australia. Maribels label " Vorine by Quint " is based upon taking old world design techniques and infusing them modern twist. The card design should incorporate an old world theme using colours like mustard, ocha, black, white and elements of lace pattern.

Card Details:

Maribel Quint
Fashion Designer
P: 04 0152 6847
E: vorinebyquint@mailbrook.com
W: www.friendsnet.com/VOrineByQuint

```html
<!DOCTYPE html>
<html lang="en">
<head>
<meta charset="utf-8">
<title>Vorine by Quint — Business Card</title>
<link rel="stylesheet" href="https://fonts.googleapis.com/css2?family=Pinyon+Script&family=Didact+Gothic&display=swap">
<style>
  :root {
    --backdrop: #d9d4c8;
    --card-dark: #1c1a0c;
    --card-mid: #2d2a18;
    --mustard: #c9c233;
  }
  * { margin: 0; padding: 0; box-sizing: border-box; }
  html, body {
    width: 1200px;
    height: 1181px;
    overflow: hidden;
    background: var(--backdrop);
  }
  .canvas {
    position: relative;
    width: 1200px;
    height: 1181px;
  }
  .card {
    position: absolute;
    left: 220px;
    width: 760px;
    height: 440px;
    border-radius: 28px;
    overflow: hidden;
    background: radial-gradient(ellipse at center, var(--card-mid) 0%, var(--card-dark) 70%);
    box-shadow: 0 4px 14px rgba(0, 0, 0, 0.25);
    color: var(--mustard);
    text-align: center;
  }
  .card--front { top: 115px; }
  .card--back { top: 617px; }
  .card__art {
    position: absolute;
    inset: 0;
    width: 100%;
    height: 100%;
  }
  .cartouche {
    fill: none;
    stroke: var(--mustard);
    stroke-width: 7;
    stroke-linejoin: round;
    stroke-linecap: round;
  }
  .label-name {
    position: absolute;
    top: 194px;
    left: 0;
    right: 0;
    font-family: "Pinyon Script", cursive;
    font-weight: 400;
    font-size: 54px;
    line-height: 1;
    letter-spacing: 1px;
  }
  .designer-name {
    position: absolute;
    top: 194px;
    left: 0;
    right: 0;
    font-family: "Pinyon Script", cursive;
    font-weight: 400;
    font-size: 52px;
    line-height: 1;
    letter-spacing: 1px;
  }
  .designer-role {
    position: absolute;
    top: 243px;
    left: 0;
    right: 0;
    font-family: "Didact Gothic", sans-serif;
    font-size: 20px;
    letter-spacing: 4px;
  }
  .contact {
    position: absolute;
    top: 377px;
    left: 0;
    right: 0;
    list-style: none;
    font-family: "Didact Gothic", sans-serif;
    font-size: 13px;
    line-height: 17px;
  }
</style>
</head>
<body>
<main class="canvas">

  <section class="card card--front">
    <svg class="card__art" viewBox="0 0 760 440">
      <defs>
        <radialGradient id="scroll-tone-front">
          <stop offset="0%" stop-color="#c9c233" stop-opacity="0.45"/>
          <stop offset="100%" stop-color="#c9c233" stop-opacity="0"/>
        </radialGradient>
      </defs>
      <g role="img" aria-label="Mustard baroque scrolls and leaves surrounding the frame">
        <ellipse cx="225" cy="95" rx="120" ry="80" fill="url(#scroll-tone-front)"/>
        <ellipse cx="535" cy="95" rx="120" ry="80" fill="url(#scroll-tone-front)"/>
        <ellipse cx="225" cy="345" rx="120" ry="80" fill="url(#scroll-tone-front)"/>
        <ellipse cx="535" cy="345" rx="120" ry="80" fill="url(#scroll-tone-front)"/>
        <ellipse cx="60" cy="220" rx="70" ry="70" fill="url(#scroll-tone-front)"/>
        <ellipse cx="700" cy="220" rx="70" ry="70" fill="url(#scroll-tone-front)"/>
      </g>
      <path class="cartouche" d="M110 220 C140 200 150 160 190 150 C230 140 220 95 280 95 C330 95 350 80 380 80 C410 80 430 95 480 95 C540 95 530 140 570 150 C610 160 620 200 650 220 C620 240 610 280 570 290 C530 300 540 345 480 345 C430 345 410 360 380 360 C350 360 330 345 280 345 C220 345 230 300 190 290 C150 280 140 240 110 220 Z"/>
    </svg>
    <h1 class="label-name">Vorine by Quint</h1>
  </section>

  <section class="card card--back">
    <svg class="card__art" viewBox="0 0 760 440">
      <defs>
        <radialGradient id="scroll-tone-back">
          <stop offset="0%" stop-color="#c9c233" stop-opacity="0.45"/>
          <stop offset="100%" stop-color="#c9c233" stop-opacity="0"/>
        </radialGradient>
      </defs>
      <g role="img" aria-label="Mustard baroque scrolls and leaves surrounding the frame">
        <ellipse cx="225" cy="95" rx="120" ry="80" fill="url(#scroll-tone-back)"/>
        <ellipse cx="535" cy="95" rx="120" ry="80" fill="url(#scroll-tone-back)"/>
        <ellipse cx="200" cy="360" rx="90" ry="80" fill="url(#scroll-tone-back)"/>
        <ellipse cx="560" cy="360" rx="90" ry="80" fill="url(#scroll-tone-back)"/>
        <ellipse cx="60" cy="220" rx="70" ry="70" fill="url(#scroll-tone-back)"/>
        <ellipse cx="700" cy="220" rx="70" ry="70" fill="url(#scroll-tone-back)"/>
      </g>
      <path class="cartouche" d="M200 440 C205 370 170 330 150 300 C130 270 120 240 110 220 C140 200 150 160 190 150 C230 140 220 95 280 95 C330 95 350 80 380 80 C410 80 430 95 480 95 C540 95 530 140 570 150 C610 160 620 200 650 220 C640 240 630 270 610 300 C590 330 555 370 560 440"/>
    </svg>
    <h2 class="designer-name">Maribel Quint</h2>
    <p class="designer-role">Fashion Designer</p>
    <ul class="contact">
      <li class="contact__phone">04 0152 6847</li>
      <li class="contact__web">www.friendsnet.com/VOrineByQuint</li>
      <li class="contact__email">vorinebyquint@mailbrook.com</li>
    </ul>
  </section>

</main>
</body>
</html>
```